Need somewhat upscale, eye catching honey jar label to make our product stand out on store shelves.

We need front and back labels for a honey jar. Files "Honey Jar Front Label 2" & "Honey Jar Back Label 2" show what I have come up with.

Files "Honey Jar Front Label 2". I did this as an example. It shows the information that needs to be included on the front label. The picture was taken by my daughter. The information and picture can be rearranged, enlarged, reduced, cropped, etc. as you see fit.

Files "Honey Jar Back Label 2". I did this one to play with the wording to get the information to fit. It explains how I keep bees. It can be worded differently as long as all the information is included.

I know nothing about good use of color, borders, backgrounds, font style and size, etc. so please excuse my plain presentations. I admire and respect your creative abilities very much.

Since my method of keeping bees involves a lot of travel time and expense, as mentioned in files "Honey Jar Back Label 2" I will try to price my honey a little higher than the competition so please design accordingly with that in mind.

We think we want to use a traditional jar with stick on labels like Marlow's jar seen in file Marlow's Jar. However, feel free to use a different jar as long as the honey can be easily scooped out with a spoon and does not have to be poured out. I know that eliminates a lot of fancy jars but that's what my customers want. Jar size should be 12 ounces which will hold a little more than 1 pound of honey.

Hanging labels are also acceptable therefore jar shapes that will not accept a stick on label can also be used. An example is a Honeypot Jar.

And of course we like Hexagon Jars which are 6 sided like the cells in honeycomb.

Please stick to glass jars that are readily available. No custom shaped jars for now.

Marlow's jar is clear glass and the metal lid is a light golden color.

It's probably a good idea for the shape of the labels to match the shape of the bottle like I marked in black on Marlow's Jar. Being wider in the middle should allow the back label to be shorter than my example seen in files "Honey Jar Back Label 2". I think front and back labels should be the same size.

The shape of the area marked in black around Marlow's label measures 1-1/4 (1.25) inches across the top, 2-1/4 (2.25) inches across the middle, 2 inches across the bottom and 3-1/2 (3.5) inches tall from top to bottom.

Target Market(s)

People wanting local honey that is not processed in any way.
People that are willing to pay a little more for honey from bees that are kept in a sustainable way (see the story in files 2 & 17) without the use of harsh chemicals.

Industry/Entity Type

Travel

Font styles to use
Serif
Decorative
Script

Requirements
Must have
• See my lengthy project description, file "Honey Jar Front Label 2" and file "Honey Jar Back Label 2". All of the info. therein is very important.
• Somewhat upscale, eye catching appearance that makes the product stand out on store shelves and suggests that the honey inside is quality, unprocessed truly local honey.
Nice to have
• If bullets are used they can look like a skep (type of beehive). I have included an example in a file.
• Swirly dashed line coming off the s in lin-Wren's with a honeybee at the end of it. See files for examples.
• Swirly dashed line coming off the i in wildflower making the shape of a heart with a honeybee at the end of it hovering over the o in wildflower and the o looks like a flower. See files for examples.

```html
<!DOCTYPE html>
<html lang="en">
<head>
<meta charset="utf-8">
<title>Lin-Wren's Local Honey – Front Label</title>
<link href="https://fonts.googleapis.com/css2?family=Comic+Neue:wght@700&family=Mansalva&family=Courier+Prime:wght@700&family=Arimo:wght@700&family=Tinos:ital,wght@0,700;1,700&display=swap" rel="stylesheet">
<style>
  :root {
    --page: #ffffff;
    --gold-dark: #a77a12;
    --gold: #e1b02a;
    --gold-light: #f7dc6a;
    --label-center: #ffec4d;
    --label-edge: #f5b400;
    --ribbon: #f39a1e;
    --ribbon-dark: #c96f0f;
    --ribbon-text: #fff6d8;
    --ink: #1a1208;
    --orange: #ee7a12;
    --white: #ffffff;
    --leaf: #2f5a1c;
    --leaf-light: #8aa546;
    --petal: #e26f8c;
    --comb: #f8d51c;
  }
  * { margin: 0; padding: 0; box-sizing: border-box; }
  html, body {
    width: 796px; height: 1200px; overflow: hidden;
    background: var(--page);
  }
  .canvas { position: relative; width: 796px; height: 1200px; }

  .label {
    position: absolute; left: 140px; top: 40px;
    width: 516px; height: 1120px;
  }
  .label-frame { position: absolute; inset: 0; }

  .label-inner {
    position: absolute; left: 22px; top: 22px; right: 22px; bottom: 22px;
    border-radius: 236px / 320px;
    overflow: hidden;
  }

  .brand {
    position: absolute; top: 92px; left: 0; right: 0;
    display: flex; justify-content: center; align-items: center; gap: 10px;
    font-family: "Comic Neue", "Comic Sans MS", cursive;
    font-weight: 700; font-size: 30px; color: var(--ink);
  }
  .brand-dot {
    width: 14px; height: 14px; border-radius: 50%;
    background: var(--white); border: 2px solid var(--gold);
  }

  .product-name {
    position: absolute; top: 150px; left: 0; right: 0;
    text-align: center; white-space: nowrap;
    font-family: "Mansalva", cursive;
    font-size: 70px; line-height: 1; color: var(--white);
    -webkit-text-stroke: 2px var(--ink);
    paint-order: stroke fill;
  }

  .ribbon { position: absolute; left: 0; top: 268px; width: 472px; height: 110px; }
  .ribbon-percent {
    position: absolute; top: 278px; left: 0; right: 0; text-align: center;
    font-family: "Courier Prime", "Courier New", monospace;
    font-weight: 700; font-size: 28px; color: var(--ribbon-text);
  }
  .ribbon-claim {
    position: absolute; top: 318px; left: 0; right: 0; text-align: center;
    font-family: "Courier Prime", "Courier New", monospace;
    font-weight: 700; font-size: 20px; color: var(--ribbon-text);
  }

  .photo {
    position: absolute; left: 0; right: 0; top: 398px; height: 346px;
    background:
      linear-gradient(to top, var(--comb) 0%, rgba(248,213,28,0.85) 22%, rgba(248,213,28,0) 45%),
      radial-gradient(ellipse 30% 36% at 58% 66%, var(--petal) 0%, rgba(226,111,140,0) 100%),
      radial-gradient(ellipse 70% 80% at 50% 40%, var(--leaf-light) 0%, var(--leaf) 75%);
    -webkit-mask-image: linear-gradient(to bottom, transparent 0%, #000 18%, #000 100%);
            mask-image: linear-gradient(to bottom, transparent 0%, #000 18%, #000 100%);
  }

  .claim-main {
    position: absolute; top: 786px; left: 0; right: 0; text-align: center;
    font-family: "Arimo", Arial, sans-serif;
    font-weight: 700; font-size: 31px; color: var(--orange);
  }
  .claim-sub {
    position: absolute; top: 826px; left: 0; right: 0; text-align: center;
    font-family: "Tinos", "Times New Roman", serif;
    font-style: italic; font-weight: 700; font-size: 21px; color: var(--ink);
  }
  .net-weight {
    position: absolute; top: 892px; left: 0; right: 0; text-align: center;
    font-family: "Tinos", "Times New Roman", serif;
    font-weight: 700; font-size: 27px; line-height: 1.4; color: var(--ink);
  }
</style>
</head>
<body>
<div class="canvas">
  <div class="label">
    <svg class="label-frame" width="516" height="1120" viewBox="0 0 516 1120">
      <defs>
        <radialGradient id="labelFill" cx="50%" cy="45%" r="60%">
          <stop offset="0%" stop-color="#ffec4d"/>
          <stop offset="100%" stop-color="#f5b400"/>
        </radialGradient>
        <linearGradient id="rimFill" x1="0" y1="0" x2="1" y2="1">
          <stop offset="0%" stop-color="#f7dc6a"/>
          <stop offset="50%" stop-color="#e1b02a"/>
          <stop offset="100%" stop-color="#a77a12"/>
        </linearGradient>
      </defs>
      <rect x="1" y="1" width="514" height="1118" rx="257" ry="342" fill="url(#rimFill)" stroke="#a77a12" stroke-width="2"/>
      <rect x="22" y="22" width="472" height="1076" rx="236" ry="320" fill="url(#labelFill)" stroke="#a77a12" stroke-width="1.5"/>
    </svg>

    <div class="label-inner">
      <div class="photo" role="img" aria-label="Photograph of a honeybee gathering pollen from a pink flower over a yellow honeycomb pattern"></div>

      <div class="brand"><span class="brand-name">Lin-Wren's</span><span class="brand-dot"></span></div>
      <div class="product-name">Local Honey</div>

      <svg class="ribbon" width="472" height="110" viewBox="0 0 472 110">
        <polygon points="14,34 70,34 70,102 14,102 32,68" fill="#c96f0f"/>
        <polygon points="458,34 402,34 402,102 458,102 440,68" fill="#c96f0f"/>
        <rect x="46" y="6" width="380" height="86" fill="#f39a1e"/>
      </svg>
      <div class="ribbon-percent">100%</div>
      <div class="ribbon-claim">Pure, Raw, Unaltered</div>

      <div class="claim-main">Never Heated</div>
      <div class="claim-sub">Strained Not Micro-Filtered</div>
      <div class="net-weight">Net Weight<br>16 oz / 454g</div>
    </div>
  </div>
</div>
</body>
</html>
```